Corporate services company needs a brochure

We are starting a company offering setup services to companies new to that location.
This includes services such as recruitment, company formation, advertising, marketing, pr, handling legal issues, logistics, transportation, procurement,immigration services, corporate gifts, accomodation,entertainment, training, administrative services etc.
Basically taking the setup issues off the hands of the company allowing them focus on their core business.

We are looking to design a professional brochure which would give the potential customers the confidence to entrust us with their needs.

We will be including some copy that can be used but i would very much like for you to bring what i have written to life - adding, deducting and amending where required.

We are looking at a A4 4/6 paged brochure but open to suggestions.

                                       

If you have any images that are suitable, please let us know. We will also be searching for some to add.

The first prize has been increased.

Thanks

Reason: We have just guaranteed the payment and we are hoping that this will encourage good designers to participate.

Reason: Some designers have requested more time to complete their final design.

Hi, I h extended the deadline to give designers more time to work on designs.

we are also looking at making the brochure a height of 8.5 and a width of 11. Please let me know your thoughts on this as any advice will help. The whole objective is to make it look as up to date and creative as possible. There is also another design size of 7.5 by 8.5

Thanks

                                        Hi

The copy has been revised and uploaded.

Hopefully it will give a clearer explanation of what we are trying to do.

Please let me know if you have any further questions.

Thanks

Marta

Reason: adding finishing touches to designs

Reason: We are amending the copy for the brochure

Reason: The new copy for the brochure is ready. I am sorry it has taken so long to get it out. I am sure we will not be making any amendments to it post today. Thanks for your patience The extension is not to attact new designs it is for existing designs's copy to be modified to include information from the updated copy.

Target Market(s)

medium to large companies in banking, telecom, retail etc. It will be viewed by middle and top management.

Industry/Entity Type

Legal

Requirements
Must have
• The brochure must clearly highlight all our services without just listing as this would risk it appearing as if we have just included everything we could think of!,
Please do not do the sitting round the conference table brochure or the typical blue and white brochure.
I desperately need it to be different, unique and serious enough to show that we are capable of handling/managing all what we have included.
Our clients include the many companies starting up an office in Africa.
We are anxious to have the potential clients understand that we will help them setup under any climax/
Nice to have
• modern colours but not too bright. there must still be a clear serious edge to it.
Should not have
• conference room table and people sitting around it.
the typical blue and white brochures often used for these type of services.

```html
<!DOCTYPE html>
<html lang="en">
<head>
<meta charset="utf-8">
<title>Corvane Brochure – Who are we?</title>
<link href="https://fonts.googleapis.com/css2?family=Source+Sans+3:ital,wght@0,300;0,400;0,600;0,700;1,700&display=swap" rel="stylesheet">
<style>
  :root {
    --sand: #b39a78;
    --paper: #ffffff;
    --bronze: #7a5324;
    --bronze-dark: #7b5a2c;
    --ink: #4a4a4a;
  }
  * { margin: 0; padding: 0; box-sizing: border-box; }
  html, body { width: 1200px; height: 848px; overflow: hidden; background: var(--paper); }
  body { font-family: "Source Sans 3", "Myriad Pro", sans-serif; position: relative; }

  .cover-panel {
    position: absolute; left: 0; top: 0;
    width: 600px; height: 848px;
    background: var(--sand);
  }
  .page-number {
    position: absolute; left: 1115px; top: 0;
    width: 28px; height: 28px;
    background: var(--bronze-dark);
    color: #fff; font-size: 8px; font-weight: 700;
    display: flex; align-items: center; justify-content: center;
  }

  .intro { position: absolute; left: 657px; width: 432px; }

  .intro-title {
    top: 183px;
    font-size: 20px; font-weight: 400;
    font-variant: small-caps; letter-spacing: 0.3px;
    color: var(--bronze);
  }
  .intro-lead {
    top: 218px;
    font-size: 9.6px; line-height: 14px; font-weight: 600;
    color: var(--bronze);
  }
  .intro-body {
    top: 258px;
    font-size: 8.1px; line-height: 12.4px; font-weight: 300;
    color: var(--ink);
  }
  .intro-body p { margin-bottom: 7px; }

  .pull-quote {
    left: 652px; width: 440px;
    text-align: center;
    font-size: 10.5px; line-height: 16.5px;
    font-weight: 700; font-style: italic;
    color: var(--bronze);
  }
  .pull-quote--stop { top: 440px; }
  .pull-quote--market { top: 530px; }

  .intro-note {
    top: 496px; width: 440px;
    font-size: 8.1px; line-height: 12px; font-weight: 300;
    color: var(--ink);
  }
</style>
</head>
<body>
  <div class="cover-panel" aria-hidden="true"></div>
  <div class="page-number">1</div>

  <h1 class="intro intro-title">Who are we?</h1>

  <p class="intro intro-lead">Corvane is a professional services company providing a comprehensive range of business services, products and solutions for non-core but vital corporate requirements.</p>

  <div class="intro intro-body">
    <p>The value we generate for our clients is managing functions that are not directly related to their core business. By outsourcing your non-core activities to Corvane, you can concentrate on your key business competencies, while Corvane manages and operates the processes that may not be your core activities, but still are critical to your business.</p>
    <p>Corvane offers business value to clients combining operational excellence with deep domain expertise in key industry verticals including logistics, procurement, PR, travel, office formation, office construction/renovation.</p>
    <p>Corvane also delivers an entire spectrum of business process outsourcing services such customer care, technology solutions and industry-specific back-office and front-office processes.</p>
    <p>Our team consists of professionals with significant experience in a wide range of outsourcing solutions and is equipped with appropriate technology to ensure fast and accurate response to the processing requirements.</p>
    <p>With our services, you will receive immediate access to business infrastructure capabilities and new strategic markets without the capital investment and time delays associated with creating in-house capability.</p>
  </div>

  <p class="intro pull-quote pull-quote--stop">We are a ‘one-stop’ shop for businesses and no matter the stage of your company;<br>our services and expertise can help drive your business forward. Our customers do not have to go to multiple vendors to source these services and save on procurement costs up front.</p>

  <p class="intro intro-note">A long established and multi-faceted organization, Corvane is dedicated to the provision of a wide range of professional services.</p>

  <p class="intro pull-quote pull-quote--market">Today’s business environment is fast moving, multi-faceted and highly competitive. Business owners need the support of professionals who provide on-time, efficient solutions to help their business move forward. We aim to provide such a service.</p>
</body>
</html>
```